Kornfeldtakt.de

The ostwind-tauschhalle.de (oth) is an internet portal for the incurance industry in Germany: www.ostwind-tauschhalle.de.

We are now planning to start a new brand Kornfeldtakt.de, which will be integral part of oth, but will have own logo, navigation etc. The main topic of Kornfeldtakt.de will be the new digital way of communication between insurance companies and insurance brokers (selling companies' products).

The main content of Kornfeldtakt.de will consist of articles / blog entries and at this moment we would like to concentrate on that part of our new brand.

At the top of the page we will always have a cover story, which will be the latest published article.

Under the cover story the user will find other articles. The articles should have variable widths (1/3, 2/3, 3/3). We will also need some additional elements like newsletter subscription, articles with most clicks etc.

Please use as reference this page:
https://www.brenntal.de/

We really like how it is designed.

Here you will find the current state of our project:

https://relaunch.ostwind-tauschhalle.de/kornfeldtakt

We will also need a logo for Kornfeldtakt.de, which should include the subtitle: Stets Klar, Immer Im Takt AND powerd by ostwind-tauschhalle.de

Due to the problems with the "Pool" functionality at Formbazaar we will need more time to verify your projects in our teem - but we are on it.

```html
<!DOCTYPE html>
<html lang="de">
<head>
<meta charset="utf-8">
<title>Kornfeldtakt</title>
<link href="https://fonts.googleapis.com/css2?family=Roboto:wght@400;500;700;900&display=swap" rel="stylesheet">
<style>
:root{
  --red:#e3101a;
  --red-dark:#b8070f;
  --ink:#222;
  --text:#333;
  --muted:#666;
  --grey-bg:#eeeff1;
  --topbar:#f3f3f3;
  --dark:#2a2a2c;
  --white:#fff;
}
*{box-sizing:border-box;margin:0;padding:0}
html,body{width:1200px;height:4079px;overflow:hidden}
body{font-family:'Roboto',sans-serif;color:var(--text);background:var(--white)}
.wrap{width:976px;margin:0 auto;position:relative}

.topbar{height:43px;background:var(--topbar)}
.topbar .wrap{display:flex;justify-content:space-between;height:43px}
.search{margin-top:4px;width:398px;height:35px;border:1px solid #ccc;background:#fff;display:flex;align-items:center;justify-content:space-between;padding:0 10px;font-size:13px;color:#555}
.top-actions{display:flex;gap:4px}
.top-btn{height:43px;display:flex;align-items:center;gap:7px;color:#fff;font-size:13px;font-weight:500;justify-content:center}
.top-btn.dark{background:#222;width:155px}
.top-btn.red{background:var(--red);width:106px}

.header{height:87px;background:#fff}
.header .wrap{display:flex;justify-content:space-between;align-items:center;height:87px}
.brand{display:flex;align-items:center;gap:14px}
.brand-mark{width:64px;height:52px;background:var(--red);border-radius:6px}
.brand-name{font-size:21px;font-weight:700;color:var(--ink);letter-spacing:.5px}
.brand-tag{font-size:13px;color:#333;margin-top:3px;letter-spacing:.3px}
.nav{display:flex;gap:27px;font-size:15px;font-weight:500;color:#222;text-transform:uppercase}
.nav a{color:inherit;text-decoration:none;padding-bottom:8px;border-bottom:3px solid transparent;margin-top:11px}
.nav a.active{color:var(--red);border-color:var(--red)}

.hero{height:532px;position:relative;background:linear-gradient(100deg,#3a3530 0%,#6b5a4e 40%,#a39080 70%,#c8c0b8 100%)}
.hero-content{position:absolute;left:112px;top:200px;color:#fff}
.hero h1{font-size:25px;font-weight:500;line-height:34px;text-transform:uppercase;width:560px}
.hero .date{margin-top:10px;font-size:15px;display:flex;gap:9px;align-items:center}
.hero .arrow{position:absolute;top:250px}
.hero .dots{position:absolute;left:566px;top:494px;display:flex;gap:6px}
.hero .dots span{width:13px;height:13px;border-radius:50%;background:#fff}
.hero .dots span.on{background:var(--red);border:3px solid #fff}

.section-title{font-size:30px;font-weight:700;color:var(--ink);text-align:center;text-transform:uppercase;letter-spacing:.5px}
.latest{padding-top:92px;height:1123px}
.grid3{display:grid;grid-template-columns:repeat(3,308px);justify-content:space-between;row-gap:23px;margin-top:40px}
.card{background:#fff;box-shadow:0 0 8px rgba(0,0,0,.14);padding:7px}
.card .img{height:192px}
.card .body{padding:20px 3px 14px}
.meta{font-size:14px;color:#333;display:flex;gap:10px;align-items:center}
.card h3{font-size:17px;font-weight:500;color:var(--ink);line-height:25px;margin-top:12px}
.card p{font-size:13.5px;color:var(--muted);line-height:23px;margin-top:8px}
.more{display:flex;gap:8px;align-items:center;color:var(--red);font-size:14px;font-weight:500;margin-top:8px}

.popular{background:var(--grey-bg);height:636px;padding-top:55px}
.grid2{display:grid;grid-template-columns:478px 478px;justify-content:space-between;margin-top:30px}
.grid2 .card .img{height:261px}
.grid2 .card h3{max-width:425px}
.grid2 .card p{max-width:450px}

.trending{padding-top:87px;height:1091px}
.trend-list{width:943px;margin:34px auto 0;display:flex;flex-direction:column;gap:31px}
.trend{display:flex;background:#fff;box-shadow:0 0 8px rgba(0,0,0,.14);padding:7px;height:257px}
.trend .img{width:328px;height:243px;flex:none}
.trend .body{padding:22px 35px 0}
.trend h3{font-size:18px;font-weight:500;color:var(--ink);line-height:25px;margin-top:14px}
.trend p{font-size:13.5px;color:var(--muted);line-height:23px;margin-top:10px}

.newsletter{height:293px;background:linear-gradient(120deg,var(--red-dark) 0%,var(--red) 40%,#ee1c24 60%,var(--red-dark) 100%);text-align:center;color:#fff;padding-top:54px}
.newsletter h2{font-size:23px;font-weight:700;letter-spacing:.4px}
.newsletter p{font-size:13.5px;line-height:24px;width:760px;margin:15px auto 0}
.subscribe{display:flex;justify-content:center;gap:7px;margin-top:36px}
.subscribe .input{width:418px;height:47px;background:#fff;color:#555;font-size:14px;text-align:left;padding:15px 16px}
.subscribe .btn{width:189px;height:47px;background:#222;font-size:14px;font-weight:700;display:flex;align-items:center;justify-content:center}

.footer{height:274px;background:var(--dark);color:#fff;text-align:center;padding-top:48px}
.footer .brand{justify-content:center}
.footer .brand-name,.footer .brand-tag{color:#fff;text-align:left}
.fnav{display:flex;justify-content:center;font-size:15.5px;font-weight:500;text-transform:uppercase;margin-top:42px}
.fnav.second{margin-top:17px}
.fnav span.sep{margin:0 22px}
.copyright{border-top:1px solid #777;width:976px;margin:35px auto 0;padding-top:18px;font-size:12.5px}
</style>
</head>
<body>

<svg width="0" height="0" style="position:absolute">
  <defs>
    <symbol id="cal" viewBox="0 0 14 14"><rect x="1" y="2.5" width="12" height="10.5" fill="none" stroke="#e3101a" stroke-width="1.6"/><rect x="1" y="2.5" width="12" height="3" fill="#e3101a"/><rect x="3.5" y="0.5" width="1.6" height="3" fill="#e3101a"/><rect x="8.9" y="0.5" width="1.6" height="3" fill="#e3101a"/><rect x="3.5" y="7.5" width="2" height="2" fill="#e3101a"/><rect x="8" y="7.5" width="2" height="2" fill="#e3101a"/></symbol>
    <symbol id="go" viewBox="0 0 16 16"><circle cx="8" cy="8" r="6.5" fill="none" stroke="#e3101a" stroke-width="1.6"/><path d="M4.5 8h6M8 5.3L10.7 8 8 10.7" fill="none" stroke="#e3101a" stroke-width="1.6"/></symbol>
  </defs>
</svg>

<div class="topbar"><div class="wrap">
  <div class="search">Search KT
    <svg width="14" height="14" viewBox="0 0 14 14"><circle cx="6" cy="6" r="4.3" fill="none" stroke="#e3101a" stroke-width="2"/><path d="M9 9l4 4" stroke="#e3101a" stroke-width="2"/></svg>
  </div>
  <div class="top-actions">
    <div class="top-btn dark"><svg width="14" height="11" viewBox="0 0 14 11"><rect width="14" height="11" fill="#fff"/><path d="M0 0l7 6 7-6" fill="none" stroke="#222" stroke-width="1.4"/></svg>NEWSLETTER</div>
    <div class="top-btn red"><svg width="14" height="14" viewBox="0 0 14 14"><circle cx="7" cy="7" r="6" fill="none" stroke="#fff" stroke-width="1.5"/><circle cx="7" cy="5.5" r="2.2" fill="#fff"/><path d="M3 11.2c1-2.4 7-2.4 8 0" fill="#fff"/></svg>LOG IN</div>
  </div>
</div></div>

<header class="header"><div class="wrap">
  <div class="brand">
    <div class="brand-mark"></div>
    <div><div class="brand-name">KORNFELDTAKT</div><div class="brand-tag">Stets Klar, Immer Im Takt</div></div>
  </div>
  <nav class="nav"><a class="active">Home</a><a>Process Messages</a><a>KT Systems</a><a>Events</a><a>Studies</a></nav>
</div></header>

<section class="hero" role="img" aria-label="Photo of an insurance broker advising a client at a desk with a laptop">
  <svg class="arrow" style="left:50px" width="14" height="24" viewBox="0 0 14 24"><path d="M12 2L3 12l9 10" fill="none" stroke="#fff" stroke-width="3"/></svg>
  <svg class="arrow" style="left:1136px" width="14" height="24" viewBox="0 0 14 24"><path d="M2 2l9 10-9 10" fill="none" stroke="#fff" stroke-width="3"/></svg>
  <div class="hero-content">
    <h1>The new digital way of communication between insurance companies and insurance brokers</h1>
    <div class="date"><svg width="14" height="14"><use href="#cal"/></svg>22 Jan 2022</div>
  </div>
  <div class="dots"><span></span><span class="on"></span><span></span><span></span></div>
</section>

<section class="latest"><div class="wrap">
  <h2 class="section-title">Latest Published Article</h2>
  <div class="grid3">
    <article class="card"><div class="img" role="img" aria-label="Photo of a broker meeting with two clients" style="background:linear-gradient(135deg,#8a7a6c,#d8d0c8)"></div><div class="body"><div class="meta"><svg width="14" height="14"><use href="#cal"/></svg>22 Jan 2022</div><h3>Lorem ipsum dolor sit amet consectetur adipis</h3><p>Sed ut perspiciatis unde omnis iste natus err or sit voluptatem accusantium dolore mque laudantium totamea.</p><div class="more">Continue Reading <svg width="16" height="16"><use href="#go"/></svg></div></div></article>
    <article class="card"><div class="img" role="img" aria-label="Photo of a team discussing at a table with a laptop" style="background:linear-gradient(135deg,#6f8aa4,#d5dde4)"></div><div class="body"><div class="meta"><svg width="14" height="14"><use href="#cal"/></svg>22 Jan 2022</div><h3>Lorem ipsum dolor sit amet consectetur adipis</h3><p>Sed ut perspiciatis unde omnis iste natus err or sit voluptatem accusantium dolore mque laudantium totamea.</p><div class="more">Continue Reading <svg width="16" height="16"><use href="#go"/></svg></div></div></article>
    <article class="card"><div class="img" role="img" aria-label="Photo of a couple reviewing documents at a laptop" style="background:linear-gradient(135deg,#5a4e46,#c9c4bd)"></div><div class="body"><div class="meta"><svg width="14" height="14"><use href="#cal"/></svg>22 Jan 2022</div><h3>Lorem ipsum dolor sit amet consectetur adipis</h3><p>Sed ut perspiciatis unde omnis iste natus err or sit voluptatem accusantium dolore mque laudantium totamea.</p><div class="more">Continue Reading <svg width="16" height="16"><use href="#go"/></svg></div></div></article>
    <article class="card"><div class="img" role="img" aria-label="Photo of two colleagues working in a bright office" style="background:linear-gradient(135deg,#c9c7c0,#8c8a84)"></div><div class="body"><div class="meta"><svg width="14" height="14"><use href="#cal"/></svg>22 Jan 2022</div><h3>Lorem ipsum dolor sit amet consectetur adipis</h3><p>Sed ut perspiciatis unde omnis iste natus err or sit voluptatem accusantium dolore mque laudantium totamea.</p><div class="more">Continue Reading <svg width="16" height="16"><use href="#go"/></svg></div></div></article>
    <article class="card"><div class="img" role="img" aria-label="Photo of a client meeting with a tablet" style="background:linear-gradient(135deg,#2e4766,#b9b3ab)"></div><div class="body"><div class="meta"><svg width="14" height="14"><use href="#cal"/></svg>22 Jan 2022</div><h3>Lorem ipsum dolor sit amet consectetur adipis</h3><p>Sed ut perspiciatis unde omnis iste natus err or sit voluptatem accusantium dolore mque laudantium totamea.</p><div class="more">Continue Reading <svg width="16" height="16"><use href="#go"/></svg></div></div></article>
    <article class="card"><div class="img" role="img" aria-label="Photo of an older couple reading paperwork" style="background:linear-gradient(135deg,#78746e,#d6d2cc)"></div><div class="body"><div class="meta"><svg width="14" height="14"><use href="#cal"/></svg>22 Jan 2022</div><h3>Lorem ipsum dolor sit amet consectetur adipis</h3><p>Sed ut perspiciatis unde omnis iste natus err or sit voluptatem accusantium dolore mque laudantium totamea.</p><div class="more">Continue Reading <svg width="16" height="16"><use href="#go"/></svg></div></div></article>
  </div>
</div></section>

<section class="popular"><div class="wrap">
  <h2 class="section-title">Popular Post</h2>
  <div class="grid2">
    <article class="card"><div class="img" role="img" aria-label="Photo of two colleagues looking at a laptop" style="background:linear-gradient(135deg,#3f3a38,#b8b2ac)"></div><div class="body"><div class="meta"><svg width="14" height="14"><use href="#cal"/></svg>22 Jan 2022</div><h3>Ut enim ad minima veniam quis nostrum exercita tionem ullam corporis susci</h3><p>Perspiciatis unde omnis iste natus err or sit voluptatem accusantium dolore mque laudantium totamea.</p><div class="more">Continue Reading <svg width="16" height="16"><use href="#go"/></svg></div></div></article>
    <article class="card"><div class="img" role="img" aria-label="Photo of a team meeting in a modern office" style="background:linear-gradient(135deg,#2f3b44,#9ea7ae)"></div><div class="body"><div class="meta"><svg width="14" height="14"><use href="#cal"/></svg>22 Jan 2022</div><h3>Ut enim ad minima veniam quis nostrum exercita tionem ullam corporis susci</h3><p>Perspiciatis unde omnis iste natus err or sit voluptatem accusantium dolore mque laudantium totamea.</p><div class="more">Continue Reading <svg width="16" height="16"><use href="#go"/></svg></div></div></article>
  </div>
</div></section>

<section class="trending"><div class="wrap">
  <h2 class="section-title" style="font-size:33px">Trending Articles</h2>
  <div class="trend-list">
    <article class="trend"><div class="img" role="img" aria-label="Photo of two people reviewing a document together" style="background:linear-gradient(135deg,#d8b890,#4a5a70)"></div><div class="body"><div class="meta"><svg width="14" height="14"><use href="#cal"/></svg>22 Jan 2022</div><h3>Enim ad minima veniam quis nostrum exercitationem ullamcorporis susci</h3><p>At vero eos et accusamus et iusto odio dignissimos ducimus qui blanditiis praesen tium voluptatum deleniti atque corrupti quos dolores et quas molestias excepturi sint occaecati cupiditate non providentea.</p><div class="more">Continue Reading <svg width="16" height="16"><use href="#go"/></svg></div></div></article>
    <article class="trend"><div class="img" role="img" aria-label="Photo of a handshake at an advisory meeting" style="background:linear-gradient(135deg,#8e8476,#dcd6cc)"></div><div class="body"><div class="meta"><svg width="14" height="14"><use href="#cal"/></svg>22 Jan 2022</div><h3>Enim ad minima veniam quis nostrum exercitationem ullamcorporis susci</h3><p>At vero eos et accusamus et iusto odio dignissimos ducimus qui blanditiis praesen tium voluptatum deleniti atque corrupti quos dolores et quas molestias excepturi sint occaecati cupiditate non providentea.</p><div class="more">Continue Reading <svg width="16" height="16"><use href="#go"/></svg></div></div></article>
    <article class="trend"><div class="img" role="img" aria-label="Photo of a couple reading papers at home" style="background:linear-gradient(135deg,#4a4440,#c4beb6)"></div><div class="body"><div class="meta"><svg width="14" height="14"><use href="#cal"/></svg>22 Jan 2022</div><h3>Enim ad minima veniam quis nostrum exercitationem ullamcorporis susci</h3><p>At vero eos et accusamus et iusto odio dignissimos ducimus qui blanditiis praesen tium voluptatum deleniti atque corrupti quos dolores et quas molestias excepturi sint occaecati cupiditate non providentea.</p><div class="more">Continue Reading <svg width="16" height="16"><use href="#go"/></svg></div></div></article>
  </div>
</div></section>

<section class="newsletter">
  <h2>SUBSCRIBE OUR NEWSLETTER</h2>
  <p>At vero eos et accusamus et iusto odio dignissimos ducimus qui blanditiis praesen tium voluptatum deleniti atque corrupti quos dolores et quas molestias excepturi sint occaecati cupiditate non providentea.</p>
  <div class="subscribe"><div class="input">Email Address</div><div class="btn">SUBSCRIBE NOW</div></div>
</section>

<footer class="footer">
  <div class="brand">
    <div class="brand-mark"></div>
    <div><div class="brand-name" style="font-weight:500">KORNFELDTAKT</div><div class="brand-tag">Stets Klar, Immer Im Takt</div></div>
  </div>
  <div class="fnav">Home<span class="sep">|</span>Process Messages<span class="sep">|</span>KT Systems<span class="sep">|</span>Events<span class="sep">|</span>Studies</div>
  <div class="fnav second">Privacy<span class="sep">|</span>Conditions<span class="sep">|</span>Help<span class="sep">|</span>Site Map</div>
  <div class="copyright">© 2022 KORNFELDTAKT.DE &nbsp;|&nbsp; ALL RIGHTS RESERVED</div>
</footer>

</body>
</html>
```